Business Card Design Competition

We need a business card design for our Internet Marketing company. We require both front and back designs and the final card must be 89x53mm in size, plus crop marks to 91x55mm. Colours as per logo, plus perhaps black and/or grey (#828282).
Final text must be editable (if you can supply an editable Fireworks PNG, even better)...
FRONT TEXT:
Full Name
Position
Address Line
Suburb, State, Postcode
Phone: 0000 000 000
Mobile: 0000 000 000
Email: xxx@brimleafpromo.com.au
Web: www.brimleafpromo.com.au
Rear of card should be a fresh design plus our slogan text: "Making You Memorable" in large font, then in small text "Brimleaf Holdings Pty Ltd (ABN: 42 563 701 384)".
Target Market(s)
Small/Medium Businesses
Industry/Entity Type
Business
Look and feel
Each slider illustrates characteristics of the customer's brand and the style your logo design should communicate.

```html
<!DOCTYPE html>
<html lang="en">
<head>
<meta charset="utf-8">
<title>Brimleaf Promo – Business Card</title>
<link rel="stylesheet" href="https://fonts.googleapis.com/css2?family=Tinos:wght@400;700&display=swap">
<style>
  :root {
    --canvas: #f4f4f4;
    --card: #242424;
    --orange: #f39a1e;
    --green: #8dc63f;
    --white: #ffffff;
    --grey: #828282;
    --rule: rgba(255, 255, 255, 0.75);
  }
  * { margin: 0; padding: 0; box-sizing: border-box; }
  html, body {
    width: 1200px;
    height: 900px;
    overflow: hidden;
    background: var(--canvas);
    font-family: "Tinos", "Times New Roman", serif;
  }
  .sheet { position: relative; width: 1200px; height: 900px; }

  .card {
    position: absolute;
    left: 280px;
    width: 640px;
    height: 381px;
    background: var(--card);
    overflow: hidden;
    color: var(--white);
  }
  .card--front { top: 50px; }
  .card--back { top: 470px; }

  .card__rules { position: absolute; inset: 0; width: 100%; height: 100%; }

  /* brand name with a plain circle beside it */
  .brand { position: absolute; display: flex; align-items: center; gap: 14px; }
  .brand__dot { width: 64px; height: 64px; border-radius: 50%; background: var(--green); }
  .brand__name { font-size: 38px; font-weight: 700; color: var(--orange); line-height: 1; white-space: nowrap; }
  .card--front .brand { left: 24px; top: 34px; }

  .person { position: absolute; left: 420px; top: 60px; font-size: 20px; line-height: 1.3; font-weight: 700; }

  .phones { position: absolute; left: 132px; top: 168px; font-size: 15px; line-height: 1.35; color: var(--orange); }
  .address { position: absolute; left: 124px; top: 222px; font-size: 15px; line-height: 1.35; font-weight: 700; }
  .online { position: absolute; left: 352px; top: 272px; font-size: 15px; line-height: 1.35; }
  .online__email { color: var(--orange); }
  .online__web { color: var(--green); }

  .card--back .brand { left: 28px; top: 28px; }
  .card--back .brand__dot { width: 80px; height: 80px; }
  .slogan {
    position: absolute; left: 0; right: 0; top: 148px;
    text-align: center; font-size: 48px; font-weight: 700; letter-spacing: 0.5px;
    white-space: nowrap;
  }
  .entity {
    position: absolute; right: 64px; top: 240px;
    font-size: 14px; color: var(--grey); white-space: nowrap;
  }
</style>
</head>
<body>
<main class="sheet">

  <section class="card card--front" aria-label="Front of business card">
    <svg class="card__rules" viewBox="0 0 640 381" aria-hidden="true">
      <line x1="372" y1="0" x2="410" y2="56" stroke="var(--rule)" stroke-width="1"/>
      <line x1="0" y1="135" x2="330" y2="162" stroke="var(--orange)" stroke-width="1"/>
      <line x1="116" y1="205" x2="60" y2="381" stroke="var(--rule)" stroke-width="1"/>
      <line x1="335" y1="262" x2="335" y2="381" stroke="var(--orange)" stroke-width="1"/>
      <line x1="335" y1="262" x2="640" y2="262" stroke="var(--rule)" stroke-width="0.6" opacity="0.4"/>
    </svg>

    <div class="brand">
      <span class="brand__dot"></span>
      <span class="brand__name">Brimleaf Promo</span>
    </div>

    <div class="person">
      <p class="person__name">John Doe</p>
      <p class="person__role">Marketing Manager</p>
    </div>

    <div class="phones">
      <p>Phone: 0000 000 000</p>
      <p>Mobile: 0000 000 000</p>
    </div>

    <div class="address">
      <p>314 East Harbor Lane</p>
      <p>Dayton, Ohio, 45402</p>
    </div>

    <div class="online">
      <p class="online__email">Email: xxx@brimleafpromo.com.au</p>
      <p class="online__web">Web: www.brimleafpromo.com.au</p>
    </div>
  </section>

  <section class="card card--back" aria-label="Back of business card">
    <svg class="card__rules" viewBox="0 0 640 381" aria-hidden="true">
      <line x1="72" y1="222" x2="64" y2="381" stroke="var(--rule)" stroke-width="1"/>
      <line x1="600" y1="0" x2="608" y2="381" stroke="var(--rule)" stroke-width="1"/>
    </svg>

    <div class="brand">
      <span class="brand__dot"></span>
      <span class="brand__name">Brimleaf Promo</span>
    </div>

    <p class="slogan">"Making You Memorable"</p>
    <p class="entity">Brimleaf Holdings Pty Ltd (ABN: 42 563 701 384)</p>
  </section>

</main>
</body>
</html>
```